financial company web page

We are tax and financial consulting company that needs a web site. Our logo is attached. Headquarters of our company is based in Latvia, Riga. Our actual temporary web site is www.corvanteq.com The main purpose of our new web site is:
* to explain the benefits of doing business through Latvian LLC companies;
* provide necessary information about taxation regime in Latvia for trading and holding companies
* propose some standard schemes of using Latvian companies for various businesses.
* offer our clients other jurisdictions companies - other European, offshore, etc.
* offer our clients ecommerce solutions
* offer our client residency in Latvia and EU
Registration of a Latvian company + accounting + legal advice will be our primary product. However, web site first page should highlight 4 other important products, such as:
1 - eCommerce (here we will explain briefly what is eCommerce, how our client can use it, what are the bonuses doing business online, explain conditions of eCommerce, etc) ;
2 - Residence Permit (here we offer EU and non-EU citizens to obtain Latvian residence permit and explain the benefits of having Latvian ID card);
3 - other Jurisdictions (here we propose list of other companies registered in the countries with favorable taxation regime, i.e. UK, Hong-Kong, Canada, Panama, BVI, UAE, etc);
4 - banking (here we explain benefits of having bank account in Latvia, explaining briefly products that bank offer, etc).
Overall Website map is the following:
1. About us
2. About Latvia
3. Contacts
4. Latvian company
5. Our services
a. еCommerce
b. Resident permit (Latvia and EU)
c. Bank accounts
d. Registration and support of other jurisdictions (European companies, Low tax companies, Offshore companies)
e. Additional services (Tax advisory, Virtual office, European licenses, Accounting services, Legal address in Riga)
6. Become Partner
7. Corvanteq Travel Guide
As a start point we need only first page design. If this design suits us well we will continue to work with you on other pages. We are looking for innovative, creative and professional design in line with our corporate logo and colours. We want this design to focus more on graphic, on simplicity and usability. It should be immediately clear from the first glance what the site is about, what is our key product and how to get more information if I'm interested on something.
These are website from our sector, we want to be better:
http://www.marlowbayholdings.com/
http://www.qtr-harbourline.com/
http://www.dwpenterprisehub.com/
http://www.firmsetupnorth59.co.uk/
In case you can't find our logo, please, ask I will send it to your mail. Thanks!
Target Market(s)
European, Russian or Chinesee enterpreneurs
Industry/Entity Type
Accounting
Requirements
Must have
- Web site will be on 10 languages, so somewhere must be a button/flag to switch language.
Contact information should be on every page (phone number and add Chatterloop buttons or similar).
Search button should be available on the first page
Button Request a Call should be on every page.
Visitors should also have a possibility to download a brochure about each product (so appropriate button should be in each section).

```html
<!DOCTYPE html>
<html lang="en">
<head>
<meta charset="utf-8">
<title>Corvanteq – Tax &amp; Financial Solutions</title>
<link rel="stylesheet" href="https://fonts.googleapis.com/css2?family=Open+Sans:ital,wght@0,400;0,600;0,700;1,300;1,400&display=swap">
<style>
:root{
  --navy:#0f2d63;
  --navy-dark:#0a214b;
  --blue:#1d4f9c;
  --orange:#f7a81b;
  --orange-dark:#e08e0b;
  --grey-bg:#eeeeee;
  --grey-line:#d6d6d6;
  --text:#555b63;
  --muted:#8a8f96;
  --white:#ffffff;
}
*{box-sizing:border-box;margin:0;padding:0}
html,body{width:814px;height:1200px;overflow:hidden}
body{font-family:"Open Sans",Arial,sans-serif;color:var(--text);background:var(--grey-bg);position:relative}
.page{position:absolute;left:0;top:0;width:814px;height:1200px;background:linear-gradient(#ffffff 0,#ffffff 90px,#f3f3f3 90px,#f3f3f3 1063px)}

/* header */
.site-header{position:absolute;left:76px;top:14px;width:662px;height:60px}
.brand{display:flex;align-items:center;gap:8px;color:var(--navy);font-weight:700;font-size:27px;letter-spacing:.3px}
.brand-mark{width:22px;height:22px;border-radius:50%;background:var(--blue)}
.lang{position:absolute;right:0;top:26px;display:flex;align-items:center;gap:4px;font-size:9px;color:var(--muted)}
.lang span.label{margin-right:4px}
.flag{width:12px;height:8px;display:inline-block}

/* nav */
.main-nav{position:absolute;left:76px;top:90px;width:662px;height:20px;background:#e4e4e4;border-top:1px solid var(--grey-line);border-bottom:1px solid var(--grey-line);display:flex;align-items:center;font-size:8.5px;color:#666}
.main-nav a{color:inherit;text-decoration:none;padding:0 14px;border-right:1px solid #cfcfcf;line-height:12px}
.search{margin-left:auto;margin-right:6px;display:flex;align-items:center;gap:4px}
.search-field{width:90px;height:13px;background:#fff;border:1px solid #ccc;font-size:7.5px;padding-left:4px;line-height:11px;color:#999}

/* hero */
.hero{position:absolute;left:76px;top:123px;width:662px;height:232px}
.hero-photo{position:absolute;left:0;top:0;width:467px;height:232px;background:linear-gradient(110deg,#3b4a5c 0%,#8795a5 35%,#d8d3cc 60%,#efe9e2 100%)}
.hero-caption{position:absolute;left:50px;top:38px;width:250px;color:#fff;font-size:20px;line-height:22px;font-weight:600;text-shadow:0 1px 3px rgba(0,0,0,.4)}
.hero-arrow{position:absolute;top:100px;width:20px;height:30px;background:rgba(255,255,255,.85);display:flex;align-items:center;justify-content:center}
.hero-arrow.prev{left:0}.hero-arrow.next{left:447px}
.callback{position:absolute;left:475px;top:0;width:187px;height:232px;background:var(--navy);padding:14px 16px;color:#fff}
.callback h2{font-size:17px;font-weight:700;margin-bottom:16px}
.callback label{display:block;font-size:9.5px;margin-bottom:4px}
.callback .field{height:20px;background:#fff;margin-bottom:12px}
.btn{display:inline-block;background:linear-gradient(var(--orange),var(--orange-dark));color:#fff;font-weight:700;border-radius:2px;text-align:center;white-space:nowrap}
.callback .btn{width:100px;height:22px;line-height:22px;font-size:10.5px;margin-top:4px}

/* tagline */
.tagline{position:absolute;left:76px;top:382px;width:662px;text-align:center;font-style:italic;font-weight:300;color:#8a8a8a;font-size:21px;line-height:26px}

/* service cards */
.services{position:absolute;left:76px;top:452px;width:662px;display:flex;gap:14px}
.service-card{flex:1;height:134px;background:#fff;border:1px solid var(--grey-line);padding:12px 12px}
.service-head{display:flex;align-items:center;gap:8px;margin-bottom:10px}
.service-icon{width:42px;height:38px;border-radius:3px}
.service-card h3{font-size:15px;font-weight:400;color:#7a7f86;white-space:nowrap}
.service-card p{font-size:8px;line-height:11px;color:#9a9ea4;margin-left:50px;margin-bottom:6px}
.service-card .btn{margin-left:50px;width:50px;height:14px;line-height:14px;font-size:7.5px}

/* why box */
.why{position:absolute;left:76px;top:605px;width:460px;height:345px;background:#fff;border:1px solid var(--grey-line);padding:12px 16px}
.why h2,.testimonials h2{font-size:13px;font-weight:400;color:#7a7f86;padding-bottom:8px;border-bottom:1px solid #e3e3e3}
.why-item{display:flex;gap:16px;margin-top:22px}
.why-photo{width:150px;height:100px;flex:none}
.why-item p{font-size:8.5px;line-height:12px;color:#9a9ea4;margin-bottom:8px}
.why-item .btn{width:52px;height:15px;line-height:15px;font-size:7.5px}

/* right column */
.testimonials{position:absolute;left:546px;top:605px;width:192px;height:213px;background:#fff;border:1px solid var(--grey-line);padding:12px 14px}
.quote{display:flex;gap:10px;margin-top:16px}
.quote-photo{width:34px;height:40px;flex:none;background:linear-gradient(#7b8796,#c9c1b6)}
.quote p{font-size:8px;line-height:11px;color:#9a9ea4}
.brochure{position:absolute;left:546px;top:832px;width:192px;height:118px;background:#c9c9c9;border:1px solid #bcbcbc}
.brochure-cover{position:absolute;left:14px;top:16px;width:58px;height:78px;background:linear-gradient(160deg,#ffffff,#d8342c 70%)}
.brochure h3{position:absolute;left:80px;top:20px;font-size:15px;line-height:20px;font-weight:400;color:#fff;white-space:nowrap}
.brochure .btn{position:absolute;left:90px;top:54px;width:78px;height:20px;line-height:20px;font-size:9px}

/* partners */
.partners{position:absolute;left:76px;top:985px;width:662px;height:36px;display:flex;align-items:center;justify-content:space-between}
.partner-badge{height:26px;background:#c7ccd3;border-radius:2px}
.arrow-round{width:16px;height:16px;border-radius:50%;background:#c2c6cc;display:flex;align-items:center;justify-content:center}

/* footer */
.site-footer{position:absolute;left:0;top:1063px;width:814px;height:117px;background:var(--navy);color:#fff}
.footer-inner{position:absolute;left:76px;top:14px;width:662px;display:flex}
.footer-col{width:150px;font-size:8.5px;line-height:16px}
.footer-col h4{font-size:10px;font-weight:600;margin-bottom:4px}
.footer-col li{list-style:none;padding-left:10px;position:relative}
.footer-col li::before{content:"";position:absolute;left:0;top:6px;width:4px;height:4px;background:#8fa6d0}
.footer-brand{margin-left:auto;margin-top:22px;display:flex;align-items:center;gap:8px;font-weight:700;font-size:25px}
.footer-brand .brand-mark{background:#fff}
.copyright{position:absolute;left:0;top:1180px;width:814px;height:20px;background:var(--navy-dark);color:#c8d2e6;font-size:8px;line-height:20px;padding-left:76px}
</style>
</head>
<body>
<div class="page">

  <header class="site-header">
    <div class="brand"><span class="brand-mark"></span>Corvanteq</div>
    <div class="lang">
      <span class="label">Select Your Language</span>
      <i class="flag" style="background:#c8102e"></i>
      <i class="flag" style="background:#1f4aa8"></i>
      <i class="flag" style="background:#e03c31"></i>
      <i class="flag" style="background:#0055a4"></i>
      <i class="flag" style="background:#ffce00"></i>
      <i class="flag" style="background:#de2910"></i>
      <i class="flag" style="background:#009246"></i>
      <i class="flag" style="background:#9e3039"></i>
    </div>
  </header>

  <nav class="main-nav">
    <a>About Us</a><a>About Latvia</a><a>Contacts</a><a>Latvian company</a><a>Our services</a><a>Become Partner</a>
    <div class="search"><span>Search Here</span><span class="search-field">Search</span></div>
  </nav>

  <section class="hero">
    <div class="hero-photo" role="img" aria-label="Smiling businesswoman in front of colleagues in a bright office"></div>
    <p class="hero-caption">All our package prices INCLUDE the 1st year company fees</p>
    <span class="hero-arrow prev"><svg width="8" height="12" viewBox="0 0 8 12"><path d="M7 1 2 6l5 5" stroke="#555" stroke-width="2" fill="none"/></svg></span>
    <span class="hero-arrow next"><svg width="8" height="12" viewBox="0 0 8 12"><path d="M1 1l5 5-5 5" stroke="#555" stroke-width="2" fill="none"/></svg></span>
    <form class="callback">
      <h2>Request a Call</h2>
      <label>Your Name</label><div class="field"></div>
      <label>Your Email</label><div class="field"></div>
      <span class="btn">Request Call</span>
    </form>
  </section>

  <p class="tagline">We're not just here to set your business up, but<br>to support you as it grows...</p>

  <section class="services">
    <article class="service-card">
      <div class="service-head"><div class="service-icon" role="img" aria-label="Bank building icon" style="background:linear-gradient(#9cc36a,#5f8f2f)"></div><h3>Bank Account</h3></div>
      <p>Quick help opening a business account with partner banks in the EU.</p>
      <span class="btn">Read More</span>
    </article>
    <article class="service-card">
      <div class="service-head"><div class="service-icon" role="img" aria-label="Magnifying glass icon" style="background:linear-gradient(#e6e9ee,#aeb5bf)"></div><h3>Company Searches</h3></div>
      <p>Check any registered firm and get its full record within one day.</p>
      <span class="btn">Read More</span>
    </article>
    <article class="service-card">
      <div class="service-head"><div class="service-icon" role="img" aria-label="Cardboard box icon" style="background:linear-gradient(#e2c48f,#b98a46)"></div><h3>Offshore Services</h3></div>
      <p>Set up low tax companies in trusted jurisdictions with full support.</p>
      <span class="btn">Read More</span>
    </article>
  </section>

  <section class="why">
    <h2>Why Use Our Company Registration</h2>
    <div class="why-item">
      <div class="why-photo" role="img" aria-label="Laptop and documents on a desk" style="background:linear-gradient(135deg,#2b3442,#6b7787 60%,#b9c0c8)"></div>
      <div><p>We register your Latvian company fast, handle the paperwork and keep your accounts in order from the very first day.</p><span class="btn">Read More</span></div>
    </div>
    <div class="why-item">
      <div class="why-photo" role="img" aria-label="Financial charts with a pen" style="background:linear-gradient(135deg,#dfe6ee,#7d98bb 60%,#3a5f8f)"></div>
      <div><p>Our advisers explain local tax rules in plain words and build a structure that fits the way you trade.</p><span class="btn">Read More</span></div>
    </div>
  </section>

  <aside class="testimonials">
    <h2>What they Say</h2>
    <div class="quote"><div class="quote-photo" role="img" aria-label="Portrait of a client"></div><p>Clear advice and a fast setup. Our Riga firm was ready in a week.</p></div>
    <div class="quote"><div class="quote-photo" role="img" aria-label="Portrait of a client"></div><p>Clear advice and a fast setup. Our Riga firm was ready in a week.</p></div>
  </aside>

  <aside class="brochure">
    <div class="brochure-cover" role="img" aria-label="Brochure cover"></div>
    <h3>Our Brochure</h3>
    <span class="btn">DOWNLOAD</span>
  </aside>

  <section class="partners" aria-label="Partners">
    <span class="arrow-round"><svg width="6" height="8" viewBox="0 0 6 8"><path d="M5 0 0 4l5 4z" fill="#fff"/></svg></span>
    <span class="partner-badge" style="width:26px;border-radius:50%"></span>
    <span class="partner-badge" style="width:48px"></span>
    <span class="partner-badge" style="width:62px"></span>
    <span class="partner-badge" style="width:66px"></span>
    <span class="partner-badge" style="width:30px;border-radius:50%"></span>
    <span class="partner-badge" style="width:50px"></span>
    <span class="partner-badge" style="width:44px"></span>
    <span class="arrow-round"><svg width="6" height="8" viewBox="0 0 6 8"><path d="M1 0l5 4-5 4z" fill="#fff"/></svg></span>
  </section>

  <footer class="site-footer">
    <div class="footer-inner">
      <div class="footer-col"><h4>Navigation</h4><ul><li>About Us</li><li>Why Corvanteq</li><li>FAQ</li></ul></div>
      <div class="footer-col"><h4>&nbsp;</h4><ul><li>Tips To Using Our System</li><li>Contact us</li><li>Terms of Use</li></ul></div>
      <div class="footer-col"><h4>Get in Touch</h4><ul><li>Tips To Using Our System</li><li>Contact us</li><li>Terms of Use</li></ul></div>
      <div class="footer-brand"><span class="brand-mark"></span>Corvanteq</div>
    </div>
  </footer>
  <div class="copyright">Corvanteq 2013 Copyright All rights Reserved</div>

</div>
</body>
</html>
```